Business card for Tolvery Anesthesia LLC

This is for a business care for Tolvery Anesthesia LLC. Dr. Lisbeth Tolvery, CRNA, DNAP is the sole provider in the LLC. Business address is 4718 N Brackley Street,
Oakhaven, PA 17342
CRNA stands for certified registered nurse anesthetist
"Keeping you safe and comfortable"
I plan to give this business card to the patients that I provide anesthesia to.
Creative design that ties into Anesthesia. Calm soothing colors.

Target Market(s)

Business card for my patients.

Industry/Entity Type

Medicine

Contact Information for Business Card

Creative, professional, eye catching

Logo Text

Tolvery Anesthesia

Font styles to use
Serif
Script

Colors

Designer to choose colors to be used in the design.

Requirements
Must have
• Tolvery Anesthesia
• Dr. Lisbeth Tolvery, CRNA, DNAP
• tolvery.anesthesia@ quillmail.net
Nice to have
• "Keeping you safe and comfortable"
Should not have
• phone number

```html
<!DOCTYPE html>
<html lang="en">
<head>
<meta charset="utf-8">
<title>Tolvery Anesthesia LLC — Business Card</title>
<link href="https://fonts.googleapis.com/css2?family=Playfair+Display:wght@400&family=Allura&display=swap" rel="stylesheet">
<style>
  :root {
    --page-bg: #ececec;
    --card-stock: #f4f3f1;
    --ink: #1c1c1c;
    --frame: #6d6d6d;
    --card-shadow: rgba(0, 0, 0, 0.18);
  }
  * { margin: 0; padding: 0; box-sizing: border-box; }
  html, body {
    width: 1200px;
    height: 1200px;
    overflow: hidden;
    background: var(--page-bg);
  }
  .sheet {
    width: 1200px;
    height: 1200px;
    display: flex;
    flex-direction: column;
    align-items: center;
    justify-content: center;
    gap: 70px;
  }
  .card {
    position: relative;
    width: 840px;
    height: 480px;
    background: var(--card-stock);
    box-shadow: 0 10px 30px var(--card-shadow);
    color: var(--ink);
  }
  .card__frame {
    position: absolute;
    inset: 22px;
    border: 2px dotted var(--frame);
  }
  .serif {
    font-family: "Playfair Display", Georgia, serif;
  }

  /* Front */
  .card--front .company {
    position: absolute;
    top: 78px;
    left: 0;
    right: 0;
    text-align: center;
    font-size: 30px;
    letter-spacing: 1px;
    text-transform: uppercase;
  }
  .card--front .provider {
    position: absolute;
    top: 132px;
    left: 0;
    right: 0;
    text-align: center;
    font-family: "Allura", cursive;
    font-size: 96px;
    line-height: 1;
  }
  .card--front .credentials {
    position: absolute;
    top: 258px;
    left: 0;
    right: 0;
    text-align: center;
    font-size: 26px;
    letter-spacing: 1px;
  }
  .card--front .contact {
    position: absolute;
    left: 70px;
    bottom: 70px;
    display: flex;
    align-items: center;
    gap: 14px;
    font-size: 27px;
  }
  .contact__icon { width: 30px; height: 24px; flex: none; }

  /* Back */
  .card--back .brand-mark {
    position: absolute;
    top: 120px;
    left: 50%;
    width: 70px;
    height: 70px;
    margin-left: -35px;
    border-radius: 50%;
    background: var(--ink);
  }
  .card--back .company {
    position: absolute;
    top: 250px;
    left: 0;
    right: 0;
    text-align: center;
    font-size: 30px;
    letter-spacing: 1px;
    text-transform: uppercase;
  }
</style>
</head>
<body>
  <main class="sheet">
    <section class="card card--front" aria-label="Card front">
      <div class="card__frame"></div>
      <p class="company serif">Tolvery Anesthesia LLC</p>
      <p class="provider">Dr Lisbeth Tolvery</p>
      <p class="credentials serif">CRNA - DNAP</p>
      <p class="contact serif">
        <svg class="contact__icon" viewBox="0 0 30 24" aria-hidden="true">
          <rect x="1" y="1" width="28" height="22" fill="var(--ink)"/>
          <polyline points="2,3 15,14 28,3" fill="none" stroke="var(--card-stock)" stroke-width="2"/>
        </svg>
        <span>tolvery.anesthesia@ quillmail.net</span>
      </p>
    </section>

    <section class="card card--back" aria-label="Card back">
      <div class="card__frame"></div>
      <div class="brand-mark"></div>
      <p class="company serif">Tolvery Anesthesia LLC</p>
    </section>
  </main>
</body>
</html>
```